依頼詳細
インターネット通販の本格的な正統派バレエショップ(ヨーロッパ風)を目指していますので、それに合うデザインと同時に、色のレギュレーションなどを決めてプロっぽいホームページを作りたいと思っています。
現在のホームページは色々な色があり、色のレギュレーションが出来ていませんので、今回のリニューアルと同時にメインカラー、ザブカラー、アクセントカラーなどを決めてプロっぽいページ作成をする為に依頼をしました。

既にロゴは決めているので、添付したロゴの色とイメージに合わせて作って下さい。

サイトURL
www.kolvimeta.com
ページ数
1ページ
希望イメージ
シンプル 複雑
単色 カラフル
暗い 明るい
日常 高級
遊び心 厳粛
未来的 伝統的
女性的 男性的
希望する色
紫系、白のベースカラーにロゴ色である藤色をサブカラーと考えています。
納品ファイル
• イラストレーター形式 (.ai)
• フォトショップ形式 (.psd)
補足説明
ロゴを添付しました。
上部分の看板についてですが、添付しました看板を参考にお願いします。
現在のページですと看板が高く下にスクロールをしないと情報が見れないので、
直にわかるように看板を縦に短くしたいです。

報告が遅くなり大変申し訳ございませんでした。
■ 選んだ理由

ターゲットの年齢層にマッチしたデザインと、色使いがとても気に入りました。

■ 提案者全員のお礼・コメント

沢山の方がデザインをして下さり大変嬉しく思います。本当にありがとうございました。

```html
<!DOCTYPE html>
<html lang="ja">
<head>
<meta charset="utf-8">
<title>Kolvimeta バレエショップ</title>
<link href="https://fonts.googleapis.com/css2?family=Noto+Sans+JP:wght@400;500;700&family=Noto+Serif+JP:wght@500;700&family=Cormorant+Garamond:ital,wght@0,500;1,500&display=swap" rel="stylesheet">
<style>
:root{
  --purple:#8a84c0;
  --purple-dark:#5f5899;
  --lavender:#b9b5dc;
  --lavender-light:#e6e4f3;
  --lavender-pale:#f4f3fa;
  --pink:#e9c9d6;
  --text:#4a4a55;
  --muted:#8a8a96;
  --line:#d7d5e8;
  --white:#ffffff;
  --gold:#b99a6a;
}
*{box-sizing:border-box;margin:0;padding:0}
html,body{width:1200px;height:3600px;overflow:hidden}
body{font-family:"Noto Sans JP",sans-serif;color:var(--text);background:var(--white);font-size:12px;position:relative}
.topbar{height:100px;position:relative;border-bottom:1px solid var(--line)}
.tagline{position:absolute;left:14px;top:6px;font-size:11px;color:var(--muted)}
.logo{position:absolute;left:20px;top:32px;display:flex;align-items:center;gap:10px}
.logo-dot{width:26px;height:26px;border-radius:50%;background:var(--lavender)}
.logo-name{font-family:"Cormorant Garamond",serif;font-size:38px;font-weight:500;color:var(--purple-dark);letter-spacing:1px}
.contact{position:absolute;right:20px;top:10px;text-align:right}
.contact small{display:block;font-size:11px;color:var(--muted)}
.contact .tel{font-size:28px;font-weight:700;color:var(--purple-dark);letter-spacing:1px;line-height:1.3}
.contact .tel2{font-size:12px;color:var(--muted)}
.banner{height:240px;position:relative;background:linear-gradient(90deg,#f3f1f8 0%,#ecebf4 45%,#dcd8ea 100%)}
.banner-photo{position:absolute;right:0;top:0;width:640px;height:240px;background:linear-gradient(120deg,#e9e6f1,#cfc8e0 55%,#bfb6d6)}
.banner-copy{position:absolute;left:60px;top:62px;font-family:"Noto Serif JP",serif;color:var(--purple);font-size:24px;font-weight:700;line-height:1.7;letter-spacing:2px}
.nav{margin:10px 10px 0;height:76px;border:1px solid var(--line);background:var(--lavender-pale)}
.nav-main{display:flex;height:36px;border-bottom:1px solid var(--line)}
.nav-main a{flex:1;display:flex;align-items:center;justify-content:center;font-size:12px;color:var(--purple-dark);text-decoration:none;border-right:1px solid var(--line)}
.nav-cat{display:flex;height:38px;background:var(--white)}
.nav-cat a{flex:1;display:flex;align-items:center;justify-content:center;gap:6px;font-size:11px;color:var(--text);text-decoration:none}
.nav-cat i{width:14px;height:14px;border-radius:50%;background:var(--lavender);display:block}
.layout{display:grid;grid-template-columns:280px 890px;gap:20px;padding:14px 10px 0}
.side-box{border:1px solid var(--line);margin-bottom:16px}
.side-title{height:28px;background:linear-gradient(var(--lavender),var(--purple));color:var(--white);font-size:12px;font-weight:500;padding-left:12px;display:flex;align-items:center}
.side-body{padding:12px;font-size:11px;line-height:1.7}
.field{display:flex;align-items:center;gap:8px;margin-bottom:6px}
.field span{width:60px}
.field b{flex:1;height:20px;border:1px solid var(--line);background:var(--white)}
.btn{display:inline-block;background:var(--purple);color:var(--white);padding:3px 14px;font-size:11px;border-radius:2px}
.guarantee{background:var(--lavender-pale);text-align:center;padding:16px 12px}
.guarantee h3{font-family:"Noto Serif JP",serif;color:var(--purple-dark);font-size:17px;margin-bottom:8px}
.guarantee p{font-size:12px;line-height:1.9}
.colors{display:grid;grid-template-columns:1fr 1fr;gap:6px 10px}
.colors span{display:flex;align-items:center;gap:8px}
.colors i{width:28px;height:12px;display:block;border:1px solid var(--line)}
.side-banner{height:64px;margin-bottom:12px}
.feed-item{display:flex;gap:8px;padding:8px 0;border-bottom:1px dotted var(--line)}
.feed-item i{width:30px;height:30px;background:var(--lavender-light);flex:none;display:block}
.news{border:1px solid var(--line);padding:10px 14px;font-size:11px;line-height:1.9;height:56px;margin-bottom:14px}
.news b{color:var(--purple-dark);margin-right:10px}
.sec-head{height:32px;background:linear-gradient(90deg,var(--purple),var(--lavender));color:var(--white);display:flex;align-items:center;padding-left:14px;gap:10px;margin-bottom:12px}
.sec-head em{font-family:"Cormorant Garamond",serif;font-style:italic;font-size:19px}
.sec-head span{font-size:11px}
.new-row{display:grid;grid-template-columns:repeat(6,1fr);gap:10px;margin-bottom:20px}
.new-item .ph{height:76px}
.new-item p{font-size:10px;line-height:1.5;margin-top:4px;color:var(--muted)}
.rank-block{height:300px;margin-bottom:12px}
.rank-row{display:grid;grid-template-columns:repeat(6,1fr);gap:10px}
.card{position:relative}
.card .num{position:absolute;left:0;top:0;width:22px;height:22px;background:var(--gold);color:var(--white);font-size:11px;font-weight:700;display:flex;align-items:center;justify-content:center;z-index:1}
.card .ph{height:160px}
.card h4{font-size:11px;font-weight:500;color:var(--purple-dark);margin-top:6px;line-height:1.5}
.card p{font-size:10px;line-height:1.6;color:var(--muted);margin-top:3px}
.card .price{font-size:12px;color:#b0466a;font-weight:700;margin-top:3px}
.ph-a{background:linear-gradient(160deg,#f6eef2,#e3c6d3)}
.ph-b{background:linear-gradient(160deg,#f1f0f8,#c8c3e2)}
.ph-c{background:linear-gradient(160deg,#f4f1ee,#d8cfc6)}
.footer{position:absolute;left:0;bottom:0;width:1200px;height:80px;background:linear-gradient(var(--lavender),var(--purple));display:flex;align-items:center;justify-content:center}
.footer .logo-name{color:var(--white);font-size:30px}
</style>
</head>
<body>

<header class="topbar">
  <p class="tagline">バレエ経験者のスタッフがセレクトした、正統派バレエ用品の通販ショップ</p>
  <div class="logo"><span class="logo-dot"></span><span class="logo-name">Kolvimeta</span></div>
  <div class="contact">
    <small>バレエ用品のご相談はお気軽にどうぞ</small>
    <div class="tel">0120-482-715</div>
    <div class="tel2">（携帯電話から）03-5218-4406</div>
  </div>
</header>

<section class="banner">
  <div class="banner-photo" role="img" aria-label="窓辺でポーズをとるバレリーナの写真"></div>
  <p class="banner-copy">バレエ経験者のスタッフが現役の方と作品をセレクト！<br>初心者から上級者まで揃えたバレエショップ</p>
</section>

<nav class="nav">
  <div class="nav-main">
    <a>トップページ</a><a>新着商品</a><a>ランキング</a><a>送料・お支払い</a><a>サイズガイド</a><a>よくある質問</a><a>お問い合わせ</a><a>会員登録</a><a>カートを見る</a>
  </div>
  <div class="nav-cat">
    <a><i></i>レオタード</a><a><i></i>スカート</a><a><i></i>タイツ</a><a><i></i>シューズ</a><a><i></i>トウシューズ</a><a><i></i>ウォームアップ</a><a><i></i>バッグ</a><a><i></i>アクセサリー</a><a><i></i>ブランド</a><a><i></i>セール</a>
  </div>
</nav>

<div class="layout">
  <aside>
    <div class="side-box">
      <div class="side-title">会員ログイン</div>
      <div class="side-body">
        <div class="field"><span>会員ID</span><b></b></div>
        <div class="field"><span>パスワード</span><b></b></div>
        <span class="btn">ログイン</span>
        <p style="margin-top:8px">› 新規会員登録はこちら<br>› パスワードをお忘れの方</p>
      </div>
    </div>
    <div class="side-box guarantee">
      <h3>安心の3大保証</h3>
      <p>1 安心の商品交換サービス<br>2 全国送料無料キャンペーン<br>3 お急ぎ便で翌日お届け</p>
      <span class="btn" style="margin-top:10px;background:var(--gold)">詳しくはこちら</span>
    </div>
    <div class="side-box">
      <div class="side-title">フリーワード検索</div>
      <div class="side-body"><div class="field"><b></b><span class="btn" style="width:auto">検索</span></div></div>
    </div>
    <div class="side-box">
      <div class="side-title">ブランド検索</div>
      <div class="side-body">お好みのブランドから商品をお探しいただけます。一覧はこちらをご覧ください。</div>
    </div>
    <div class="side-box">
      <div class="side-title">カラー検索</div>
      <div class="side-body colors">
        <span><i style="background:#4f74c2"></i>Blue</span><span><i style="background:#ef9fbd"></i>Pink</span>
        <span><i style="background:#222"></i>Black</span><span><i style="background:#8a62b8"></i>Purple</span>
        <span><i style="background:#fff"></i>White</span><span><i style="background:#efd65a"></i>Yellow</span>
        <span><i style="background:#66ad6b"></i>Green</span><span><i style="background:#d54b4b"></i>Red</span>
        <span><i style="background:#9b9b9b"></i>Gray</span><span><i style="background:#8a5f3f"></i>Brown</span>
      </div>
    </div>
    <div class="side-banner ph-a" role="img" aria-label="発表会特集のバナー写真"></div>
    <div class="side-banner ph-b" role="img" aria-label="スタッフ紹介のバナー写真"></div>
    <div class="side-box">
      <div class="side-title">新着情報</div>
      <div class="side-body">2011.05.20 新作レオタード入荷<br>2011.05.12 夏季休業のお知らせ</div>
    </div>
    <div class="side-box">
      <div class="side-title">つぶやき</div>
      <div class="side-body">
        <div class="feed-item"><i></i><p>新作のレオタードが入荷しました。ぜひご覧ください。</p></div>
        <div class="feed-item"><i></i><p>本日は発表会用のスカートをご紹介します。</p></div>
        <div class="feed-item"><i></i><p>サイズのご相談はお電話でも承っております。</p></div>
        <div class="feed-item"><i></i><p>週末限定のセールを開催中です。</p></div>
        <div class="feed-item"><i></i><p>トウシューズの選び方をブログで更新しました。</p></div>
        <div class="feed-item"><i></i><p>お客様から素敵な舞台写真が届きました。</p></div>
        <div class="feed-item"><i></i><p>明日は定休日のため発送はお休みです。</p></div>
      </div>
    </div>
  </aside>

  <main>
    <div class="news">
      <p><b>2011.05.20</b>新作レオタード・スカートを多数入荷いたしました。詳細はこちら。</p>
      <p><b>2011.05.12</b>夏季休業期間中の発送についてのお知らせ。</p>
    </div>

    <div class="sec-head"><em>What's new</em><span>新着商品</span></div>
    <div class="new-row">
      <div class="new-item"><div class="ph ph-c" role="img" aria-label="トウシューズ用パッドの写真"></div><p>トウパッド 定番タイプ</p></div>
      <div class="new-item"><div class="ph ph-b" role="img" aria-label="バレエバッグの写真"></div><p>バレエ用トートバッグ</p></div>
      <div class="new-item"><div class="ph ph-a" role="img" aria-label="ピンクのバッグの写真"></div><p>ピンクのシューズバッグ</p></div>
      <div class="new-item"><div class="ph ph-a" role="img" aria-label="ピンクの小物入れの写真"></div><p>リボン付き小物ポーチ</p></div>
      <div class="new-item"><div class="ph ph-c" role="img" aria-label="髪留めの写真"></div><p>シニヨン用ヘアネット</p></div>
      <div class="new-item"><div class="ph ph-b" role="img" aria-label="トウシューズの写真"></div><p>トウシューズ 初心者用</p></div>
    </div>

    <section class="rank-block">
      <div class="sec-head"><em>Ranking</em><span>レオタード部門</span></div>
      <div class="rank-row">
        <div class="card"><span class="num">1</span><div class="ph ph-b" role="img" aria-label="レオタード商品写真"></div><h4>袖付きレオタード</h4><p>上品なシルエットで踊りやすい定番</p><div class="price">¥5,800</div></div>
        <div class="card"><span class="num">2</span><div class="ph ph-a" role="img" aria-label="レオタード商品写真"></div><h4>キャミソールレオタード</h4><p>背中のデザインが美しい人気品</p><div class="price">¥4,900</div></div>
        <div class="card"><span class="num">3</span><div class="ph ph-c" role="img" aria-label="レオタード商品写真"></div><h4>シンプルレオタード</h4><p>レッスン用に最適な柔らかい素材</p><div class="price">¥3,800</div></div>
        <div class="card"><span class="num">4</span><div class="ph ph-b" role="img" aria-label="レオタード商品写真"></div><h4>Vネックレオタード</h4><p>すっきり見える深めのネック</p><div class="price">¥5,200</div></div>
        <div class="card"><span class="num">5</span><div class="ph ph-a" role="img" aria-label="レオタード商品写真"></div><h4>レース付きレオタード</h4><p>発表会にも使える華やかさ</p><div class="price">¥6,500</div></div>
        <div class="card"><span class="num">6</span><div class="ph ph-c" role="img" aria-label="レオタード商品写真"></div><h4>ジュニアレオタード</h4><p>お子様向けの着やすいサイズ</p><div class="price">¥3,200</div></div>
      </div>
    </section>

    <section class="rank-block">
      <div class="sec-head"><em>Ranking</em><span>スカート部門</span></div>
      <div class="rank-row">
        <div class="card"><span class="num">1</span><div class="ph ph-a" role="img" aria-label="スカート商品写真"></div><h4>シフォン巻きスカート</h4><p>軽やかに揺れる薄手のシフォン</p><div class="price">¥2,800</div></div>
        <div class="card"><span class="num">2</span><div class="ph ph-b" role="img" aria-label="スカート商品写真"></div><h4>ロングスカート</h4><p>優雅な動きを引き立てる丈</p><div class="price">¥3,400</div></div>
        <div class="card"><span class="num">3</span><div class="ph ph-c" role="img" aria-label="スカート商品写真"></div><h4>プルオンスカート</h4><p>ゴム仕様で着脱がかんたん</p><div class="price">¥2,500</div></div>
        <div class="card"><span class="num">4</span><div class="ph ph-a" role="img" aria-label="スカート商品写真"></div><h4>二重シフォンスカート</h4><p>透け感を抑えた二枚仕立て</p><div class="price">¥3,600</div></div>
        <div class="card"><span class="num">5</span><div class="ph ph-b" role="img" aria-label="スカート商品写真"></div><h4>ショートスカート</h4><p>脚のラインがよく見える短め丈</p><div class="price">¥2,200</div></div>
        <div class="card"><span class="num">6</span><div class="ph ph-c" role="img" aria-label="スカート商品写真"></div><h4>キッズスカート</h4><p>可愛いリボン付きのお子様用</p><div class="price">¥1,900</div></div>
      </div>
    </section>

    <section class="rank-block">
      <div class="sec-head"><em>Ranking</em><span>タイツ部門</span></div>
      <div class="rank-row">
        <div class="card"><span class="num">1</span><div class="ph ph-c" role="img" aria-label="タイツ商品写真"></div><h4>コンバーチブルタイツ</h4><p>足裏に穴があり調整しやすい</p><div class="price">¥1,800</div></div>
        <div class="card"><span class="num">2</span><div class="ph ph-a" role="img" aria-label="タイツ商品写真"></div><h4>フーター付きタイツ</h4><p>毎日のレッスンに丈夫な定番</p><div class="price">¥1,500</div></div>
        <div class="card"><span class="num">3</span><div class="ph ph-b" role="img" aria-label="タイツ商品写真"></div><h4>舞台用タイツ</h4><p>光沢のある美しい仕上がり</p><div class="price">¥2,300</div></div>
        <div class="card"><span class="num">4</span><div class="ph ph-c" role="img" aria-label="タイツ商品写真"></div><h4>ジュニアタイツ</h4><p>お子様の脚にやさしく密着</p><div class="price">¥1,200</div></div>
        <div class="card"><span class="num">5</span><div class="ph ph-a" role="img" aria-label="タイツ商品写真"></div><h4>メンズタイツ</h4><p>男性向けの厚手でしっかり素材</p><div class="price">¥2,600</div></div>
        <div class="card"><span class="num">6</span><div class="ph ph-b" role="img" aria-label="タイツ商品写真"></div><h4>ストラップタイツ</h4><p>かかとを包むストラップ仕様</p><div class="price">¥1,700</div></div>
      </div>
    </section>

    <section class="rank-block">
      <div class="sec-head"><em>Ranking</em><span>シューズ部門</span></div>
      <div class="rank-row">
        <div class="card"><span class="num">1</span><div class="ph ph-a" role="img" aria-label="バレエシューズ商品写真"></div><h4>布製バレエシューズ</h4><p>足になじむ柔らかなキャンバス</p><div class="price">¥2,400</div></div>
        <div class="card"><span class="num">2</span><div class="ph ph-c" role="img" aria-label="バレエシューズ商品写真"></div><h4>革製バレエシューズ</h4><p>丈夫で長く使える本革タイプ</p><div class="price">¥3,300</div></div>
        <div class="card"><span class="num">3</span><div class="ph ph-b" role="img" aria-label="バレエシューズ商品写真"></div><h4>スプリットソール</h4><p>甲がきれいに見える分割底</p><div class="price">¥2,900</div></div>
        <div class="card"><span class="num">4</span><div class="ph ph-a" role="img" aria-label="バレエシューズ商品写真"></div><h4>キッズシューズ</h4><p>ゴム付きで脱げにくい設計</p><div class="price">¥1,800</div></div>
        <div class="card"><span class="num">5</span><div class="ph ph-c" role="img" aria-label="バレエシューズ商品写真"></div><h4>キャラクターシューズ</h4><p>ヒール付きの舞台用シューズ</p><div class="price">¥5,400</div></div>
        <div class="card"><span class="num">6</span><div class="ph ph-b" role="img" aria-label="バレエシューズ商品写真"></div><h4>ウォームアップブーツ</h4><p>足元を冷やさない防寒ブーツ</p><div class="price">¥3,900</div></div>
      </div>
    </section>

    <section class="rank-block">
      <div class="sec-head"><em>Ranking</em><span>トウシューズ部門</span></div>
      <div class="rank-row">
        <div class="card"><span class="num">1</span><div class="ph ph-c" role="img" aria-label="トウシューズ商品写真"></div><h4>初心者用トウシューズ</h4><p>はじめての一足におすすめ</p><div class="price">¥7,800</div></div>
        <div class="card"><span class="num">2</span><div class="ph ph-a" role="img" aria-label="トウシューズ商品写真"></div><h4>ソフトシャンク</h4><p>足裏の感覚をつかみやすい</p><div class="price">¥8,400</div></div>
        <div class="card"><span class="num">3</span><div class="ph ph-b" role="img" aria-label="トウシューズ商品写真"></div><h4>ハードシャンク</h4><p>しっかり支える上級者向け</p><div class="price">¥8,900</div></div>
        <div class="card"><span class="num">4</span><div class="ph ph-c" role="img" aria-label="トウシューズ商品写真"></div><h4>幅広トウシューズ</h4><p>日本人の足型に合う幅広設計</p><div class="price">¥8,200</div></div>
        <div class="card"><span class="num">5</span><div class="ph ph-a" role="img" aria-label="トウシューズ商品写真"></div><h4>トウパッド</h4><p>つま先の痛みをやわらげる</p><div class="price">¥1,600</div></div>
        <div class="card"><span class="num">6</span><div class="ph ph-b" role="img" aria-label="トウシューズ商品写真"></div><h4>リボン・ゴムセット</h4><p>トウシューズ用の縫い付け用品</p><div class="price">¥900</div></div>
      </div>
    </section>

    <section class="rank-block">
      <div class="sec-head"><em>Ranking</em><span>ウォームアップ部門</span></div>
      <div class="rank-row">
        <div class="card"><span class="num">1</span><div class="ph ph-b" role="img" aria-label="ウォームアップ商品写真"></div><h4>ニットボレロ</h4><p>肩まわりを温めるやさしい編み</p><div class="price">¥3,800</div></div>
        <div class="card"><span class="num">2</span><div class="ph ph-a" role="img" aria-label="ウォームアップ商品写真"></div><h4>サウナパンツ</h4><p>発汗を促すレッスン用パンツ</p><div class="price">¥3,200</div></div>
        <div class="card"><span class="num">3</span><div class="ph ph-c" role="img" aria-label="ウォームアップ商品写真"></div><h4>レッグウォーマー</h4><p>足首を冷えから守る定番品</p><div class="price">¥1,900</div></div>
        <div class="card"><span class="num">4</span><div class="ph ph-b" role="img" aria-label="ウォームアップ商品写真"></div><h4>ラップカーディガン</h4><p>前で結べる薄手のカーデ</p><div class="price">¥4,200</div></div>
        <div class="card"><span class="num">5</span><div class="ph ph-a" role="img" aria-label="ウォームアップ商品写真"></div><h4>ショートパンツ</h4><p>レオタードに重ねて使える</p><div class="price">¥2,600</div></div>
        <div class="card"><span class="num">6</span><div class="ph ph-c" role="img" aria-label="ウォームアップ商品写真"></div><h4>ジャンプスーツ</h4><p>全身を包む防寒ウェア</p><div class="price">¥6,800</div></div>
      </div>
    </section>

    <section class="rank-block">
      <div class="sec-head"><em>Ranking</em><span>バッグ部門</span></div>
      <div class="rank-row">
        <div class="card"><span class="num">1</span><div class="ph ph-a" role="img" aria-label="バッグ商品写真"></div><h4>レッスントート</h4><p>荷物がたっぷり入る大容量</p><div class="price">¥4,500</div></div>
        <div class="card"><span class="num">2</span><div class="ph ph-b" role="img" aria-label="バッグ商品写真"></div><h4>シューズケース</h4><p>シューズを分けて持ち運べる</p><div class="price">¥1,800</div></div>
        <div class="card"><span class="num">3</span><div class="ph ph-c" role="img" aria-label="バッグ商品写真"></div><h4>リュックタイプ</h4><p>両手が空く便利なデザイン</p><div class="price">¥5,200</div></div>
        <div class="card"><span class="num">4</span><div class="ph ph-a" role="img" aria-label="バッグ商品写真"></div><h4>キッズバッグ</h4><p>お子様に人気の可愛い刺繍</p><div class="price">¥2,900</div></div>
        <div class="card"><span class="num">5</span><div class="ph ph-b" role="img" aria-label="バッグ商品写真"></div><h4>小物ポーチ</h4><p>ヘアピンなどの収納に便利</p><div class="price">¥1,200</div></div>
        <div class="card"><span class="num">6</span><div class="ph ph-c" role="img" aria-label="バッグ商品写真"></div><h4>ガーメントケース</h4><p>衣装をしわなく持ち運べる</p><div class="price">¥3,600</div></div>
      </div>
    </section>

    <section class="rank-block">
      <div class="sec-head"><em>Ranking</em><span>アクセサリー部門</span></div>
      <div class="rank-row">
        <div class="card"><span class="num">1</span><div class="ph ph-c" role="img" aria-label="アクセサリー商品写真"></div><h4>ティアラ</h4><p>舞台を彩るきらめく髪飾り</p><div class="price">¥6,200</div></div>
        <div class="card"><span class="num">2</span><div class="ph ph-a" role="img" aria-label="アクセサリー商品写真"></div><h4>シニヨンネット</h4><p>まとめ髪をきれいに保つ</p><div class="price">¥400</div></div>
        <div class="card"><span class="num">3</span><div class="ph ph-b" role="img" aria-label="アクセサリー商品写真"></div><h4>ヘアピンセット</h4><p>しっかり留まるUピン</p><div class="price">¥500</div></div>
        <div class="card"><span class="num">4</span><div class="ph ph-c" role="img" aria-label="アクセサリー商品写真"></div><h4>髪飾りフラワー</h4><p>発表会にぴったりの花飾り</p><div class="price">¥2,100</div></div>
        <div class="card"><span class="num">5</span><div class="ph ph-a" role="img" aria-label="アクセサリー商品写真"></div><h4>チャーム</h4><p>バッグにつけられる小物</p><div class="price">¥800</div></div>
        <div class="card"><span class="num">6</span><div class="ph ph-b" role="img" aria-label="アクセサリー商品写真"></div><h4>ストレッチバンド</h4><p>柔軟性を高める練習用品</p><div class="price">¥1,500</div></div>
      </div>
    </section>

    <section class="rank-block">
      <div class="sec-head"><em>Ranking</em><span>セール部門</span></div>
      <div class="rank-row">
        <div class="card"><span class="num">1</span><div class="ph ph-b" role="img" aria-label="セール商品写真"></div><h4>限定レオタード</h4><p>数量限定のお買い得品</p><div class="price">¥2,980</div></div>
        <div class="card"><span class="num">2</span><div class="ph ph-a" role="img" aria-label="セール商品写真"></div><h4>訳ありスカート</h4><p>小さな傷ありの特価品</p><div class="price">¥1,480</div></div>
        <div class="card"><span class="num">3</span><div class="ph ph-c" role="img" aria-label="セール商品写真"></div><h4>旧モデルシューズ</h4><p>在庫限りの大特価です</p><div class="price">¥1,980</div></div>
        <div class="card"><span class="num">4</span><div class="ph ph-b" role="img" aria-label="セール商品写真"></div><h4>タイツ3足セット</h4><p>まとめ買いでお得なセット</p><div class="price">¥3,600</div></div>
        <div class="card"><span class="num">5</span><div class="ph ph-a" role="img" aria-label="セール商品写真"></div><h4>ボレロ特価</h4><p>シーズン終わりの値下げ品</p><div class="price">¥2,400</div></div>
        <div class="card"><span class="num">6</span><div class="ph ph-c" role="img" aria-label="セール商品写真"></div><h4>福袋</h4><p>人気商品を詰め合わせた袋</p><div class="price">¥5,000</div></div>
      </div>
    </section>
  </main>
</div>

<footer class="footer">
  <span class="logo-name">Kolvimeta</span>
</footer>

</body>
</html>
```